we need a business card design for a professional painting business. This company has been up and going for about ten years. However it needs an new logo. we want this business card to be modern eye catching and easy to read. I currently have been looking for VP logos but can not find one that suits our needs. This Design should be Our start to a new beginning.
Industry/Entity Type
Painting
Contact Information for Business Card
Varesko Painting Inc.
Licensed & Insured
Tomas Varesko
Phone(631)384-4562
Fax (555) 846-3021
E-mail vareskopaintinginc@mailorbit.test
Requirements
Must have
- a new logo with  VP and i would like it to be in black and white.
i would also like the front to be a solid black with the logo only and then the back to have the information.

```html
<!DOCTYPE html>
<html lang="en">
<head>
<meta charset="utf-8">
<title>Varesko Painting Inc. – Business Card</title>
<link rel="stylesheet" href="https://fonts.googleapis.com/css2?family=Oswald:wght@500&family=Arimo:wght@400;700&display=swap">
<style>
  :root {
    --backdrop: #d9d9d9;
    --card-black: #050505;
    --card-white: #ffffff;
    --mark-grey: #2a2a2a;
    --ink: #111111;
    --band-grey: #bdbdc0;
    --alert-red: #e3161d;
    --text-light: #f2f2f2;
  }
  * { box-sizing: border-box; margin: 0; padding: 0; }
  html, body {
    width: 1200px; height: 1200px; overflow: hidden;
    background: var(--backdrop);
  }
  .canvas {
    position: relative; width: 1200px; height: 1200px;
  }
  .card {
    position: absolute; left: 160px; width: 880px; height: 503px;
    box-shadow: 0 6px 20px rgba(0,0,0,0.18);
    overflow: hidden;
  }
  /* Front */
  .card-front { top: 50px; background: var(--card-black); }
  .front-brand {
    position: absolute; inset: 0;
    display: flex; flex-direction: column; align-items: center; justify-content: center;
    gap: 26px;
  }
  .front-square {
    width: 170px; height: 170px; background: var(--mark-grey);
  }
  .front-name {
    font-family: "Arimo", sans-serif; font-weight: 400;
    font-size: 30px; letter-spacing: 1px; color: var(--text-light);
  }
  /* Back */
  .card-back { top: 597px; background: var(--card-white); }
  .back-square {
    position: absolute; left: 58px; top: 62px;
    width: 134px; height: 134px; background: var(--ink);
  }
  .back-name {
    position: absolute; left: 218px; top: 58px;
    font-family: "Oswald", sans-serif; font-weight: 500;
    font-size: 50px; line-height: 1; color: var(--ink);
    transform: scaleX(0.9); transform-origin: left top;
  }
  .back-tagline {
    position: absolute; left: 228px; top: 122px;
    font-family: "Arimo", sans-serif; font-weight: 700;
    font-size: 27px; letter-spacing: 0.5px; color: var(--alert-red);
  }
  .band {
    position: absolute; left: 0; right: 0; top: 218px; height: 24px;
    background: var(--band-grey);
  }
  .contact {
    position: absolute; left: 470px; top: 272px;
    font-family: "Arimo", sans-serif; color: var(--ink);
  }
  .person-name { font-weight: 700; font-size: 30px; letter-spacing: 0.5px; }
  .person-role { font-size: 25px; margin: 4px 0 0 40px; }
  .phone-line {
    display: flex; align-items: center; gap: 10px;
    margin-top: 36px; font-size: 26px;
  }
  .phone-icon { width: 34px; height: 34px; }
  .fax-line { margin: 14px 0 0 48px; font-size: 25px; line-height: 1.05; }
  .email-line { margin-left: 48px; font-size: 22px; }
</style>
</head>
<body>
<main class="canvas">
  <section class="card card-front" aria-label="Card front">
    <div class="front-brand">
      <div class="front-square"></div>
      <p class="front-name">VARESKO PAINTING INC.</p>
    </div>
  </section>

  <section class="card card-back" aria-label="Card back">
    <div class="back-square"></div>
    <h1 class="back-name">VARESKO PAINTING INC.</h1>
    <p class="back-tagline">LICENSED AND INSURED</p>
    <div class="band"></div>
    <div class="contact">
      <p class="person-name">Tomas Varesko</p>
      <p class="person-role">Owner/Manager</p>
      <p class="phone-line">
        <svg class="phone-icon" viewBox="0 0 34 34" aria-hidden="true">
          <circle cx="17" cy="17" r="16" fill="#e6e6e6" stroke="#9a9a9a" stroke-width="1.5"/>
          <rect x="12" y="8" width="10" height="18" rx="2" fill="#333"/>
          <rect x="13.5" y="10.5" width="7" height="6" fill="#e6e6e6"/>
        </svg>
        555.217.9083
      </p>
      <p class="fax-line">Fax 555.846.3021</p>
      <p class="email-line">vareskopainting@mailorbit.test</p>
    </div>
  </section>
</main>
</body>
</html>
```